Jägerbrief
Zielgruppe
Es soll ein 'Jägerbrief' werden. Diesen Jägerbrief erhält ein Jäger, wenn er sein erstes Stück Wild auf einer Jagd erlegen konnte.
Aufgabenstellung
Das Design ist im Format einer Urkunde auszuhändigen und sollte gerne in einem traditionellen Design gemacht werden. Beispielbilder sind im Anhang und können gerne als Inspiration genommen werden.
Genaue Details:
Überschrift in groß 'Jägerbrief'
Darunter den Text zentriert wie folgt abbilden:
'Im Revier von Birkenwöhrden, gelegen im Herzen von Marschenland, tratst du,
zur Niederwildjagd an und bewiesest dein Können, deinen Respekt vor der Natur und deine Geduld im Angesicht der Herausforderung.
An diesem besonderen Tag hattest du die Ehre, deinen ersten Feldhasen zu strecken. Mit diesem Erfolg trittst du in die stolze Tradition der Waidmänner ein, die die Schönheit und den Wert unserer heimischen Wildbestände zu schätzen wissen und Verantwortung für deren Erhalt übernehmen.
Möge dieser Moment dir stets in Erinnerung bleiben und dir ein Ansporn sein, die Jagd mit Demut, Leidenschaft und Verantwortung auszuüben.
Mit diesem Jägerbrief gratulieren wir dir herzlich zu deinem ersten Feldhasen und wünschen dir weiterhin Waidmannsheil auf all deinen Wegen im Revier.
Hochachtungsvoll und mit Waidmannsgruß
Die Jagdgesellschaft von Birkenwöhrden'

```html
<!DOCTYPE html>
<html lang="de">
<head>
<meta charset="utf-8">
<title>Jägerbrief</title>
<link href="https://fonts.googleapis.com/css2?family=Arimo:wght@400&family=Federant&display=swap" rel="stylesheet">
<style>
  :root {
    --paper-top: #f5f6ee;
    --paper-bottom: #e9ede5;
    --frame-line: #9d9a8c;
    --frame-band: #d9d8cc;
    --title-green: #5f7d72;
    --body-brown: #4b2b1f;
    --rule: #b9b2a5;
    --forest-light: #c9d3cb;
    --forest-mid: #8fa599;
    --forest-dark: #6c8779;
    --hare-brown: #8a6449;
    --ribbon-tan: #c9b29a;
    --wax-red: #b8232a;
    --rope: #d8bf93;
  }
  * { margin: 0; padding: 0; box-sizing: border-box; }
  html, body { width: 849px; height: 1200px; overflow: hidden; background: var(--paper-top); }
  .certificate {
    position: relative;
    width: 849px;
    height: 1200px;
    overflow: hidden;
    background: linear-gradient(180deg, var(--paper-top) 0%, var(--paper-bottom) 100%);
    font-family: "Arimo", Arial, sans-serif;
    color: var(--body-brown);
  }
  .forest-backdrop {
    position: absolute;
    left: 0; right: 0; bottom: 0;
    height: 330px;
    background: linear-gradient(180deg, rgba(201,211,203,0) 0%, var(--forest-light) 35%, var(--forest-mid) 70%, var(--forest-dark) 100%);
  }
  .frame { position: absolute; inset: 0; pointer-events: none; }
  .frame-band {
    position: absolute;
    background: var(--frame-band);
    opacity: 0.85;
  }
  .frame-band.top    { left: 12px; right: 12px; top: 12px; height: 22px; }
  .frame-band.bottom { left: 12px; right: 12px; bottom: 12px; height: 22px; }
  .frame-band.left   { left: 12px; top: 12px; bottom: 12px; width: 22px; }
  .frame-band.right  { right: 12px; top: 12px; bottom: 12px; width: 22px; }
  .frame-line {
    position: absolute;
    border: 1.5px solid var(--frame-line);
  }
  .frame-line.outer { inset: 10px; }
  .frame-line.inner { inset: 40px; border-width: 1px; }
  .frame-line.inner-2 { inset: 44px; border-width: 1px; }
  .corner {
    position: absolute;
    width: 16px; height: 16px;
    border: 1.5px solid var(--frame-line);
    background: var(--paper-top);
  }
  .corner.tl { left: 15px; top: 15px; }
  .corner.tr { right: 15px; top: 15px; }
  .corner.bl { left: 15px; bottom: 15px; }
  .corner.br { right: 15px; bottom: 15px; }

  .title {
    position: absolute;
    left: 0; top: 50px;
    width: 849px; height: 220px;
    overflow: visible;
  }
  .title text {
    font-family: "Federant", "Georgia", serif;
    font-size: 118px;
    fill: var(--paper-top);
    stroke: var(--title-green);
    stroke-width: 7px;
    paint-order: stroke;
  }

  .body-text {
    position: absolute;
    left: 91px; width: 667px;
    text-align: center;
    font-size: 17.4px;
    line-height: 21.5px;
  }
  .opening { top: 288px; }
  .name-line {
    position: absolute;
    left: 208px; width: 455px; top: 377px;
    height: 1px;
    background: linear-gradient(90deg, rgba(185,178,165,0), var(--rule) 15%, var(--rule) 85%, rgba(185,178,165,0));
  }
  .main { top: 395px; }
  .main p + p { margin-top: 21.5px; }

  .hare-emblem {
    position: absolute;
    left: 308px; top: 702px;
    width: 230px; height: 195px;
    border-radius: 50% 50% 12px 12px;
    background: radial-gradient(ellipse at 50% 45%, var(--hare-brown) 0%, #b39a83 45%, var(--ribbon-tan) 70%, rgba(201,178,154,0) 100%);
  }

  .closing {
    position: absolute;
    left: 0; width: 849px;
    text-align: center;
    font-size: 17.4px;
    line-height: 21.5px;
  }
  .closing.greeting { top: 932px; }
  .closing.signature { top: 974px; }

  .wax-seal {
    position: absolute;
    left: 642px; top: 903px;
    width: 88px; height: 235px;
    border-radius: 44px;
    background: linear-gradient(180deg, var(--rope) 0%, var(--rope) 30%, var(--wax-red) 32%, #8f1a20 64%, var(--rope) 66%, var(--rope) 100%);
  }
</style>
</head>
<body>
<main class="certificate">
  <div class="forest-backdrop" role="img" aria-label="Waldlandschaft mit Nadelbäumen und Hügeln in Grüntönen"></div>

  <div class="frame" aria-hidden="true">
    <div class="frame-band top"></div>
    <div class="frame-band bottom"></div>
    <div class="frame-band left"></div>
    <div class="frame-band right"></div>
    <div class="frame-line outer"></div>
    <div class="frame-line inner"></div>
    <div class="frame-line inner-2"></div>
    <div class="corner tl"></div>
    <div class="corner tr"></div>
    <div class="corner bl"></div>
    <div class="corner br"></div>
  </div>

  <svg class="title" viewBox="0 50 849 220" aria-label="Jägerbrief">
    <defs>
      <path id="title-arc" d="M112 218 Q430 176 752 218"/>
    </defs>
    <text><textPath href="#title-arc" startOffset="50%" text-anchor="middle" textLength="630" lengthAdjust="spacingAndGlyphs">Jägerbrief</textPath></text>
  </svg>

  <p class="body-text opening">Im Revier von Birkenwöhrden, gelegen im Herzen von Marschenland, tratst du,</p>
  <div class="name-line" aria-hidden="true"></div>

  <div class="body-text main">
    <p>zur Niederwildjagd an und bewiesest dein Können, deinen Respekt vor der Natur und deine Geduld im Angesicht der Herausforderung.</p>
    <p>An diesem besonderen Tag hattest du die Ehre, deinen ersten Feldhasen zu strecken. Mit diesem Erfolg trittst du in die stolze Tradition der Waidmänner ein, die die Schönheit und den Wert unserer heimischen Wildbestände zu schätzen wissen und Verantwortung für deren Erhalt übernehmen.</p>
    <p>Möge dieser Moment dir stets in Erinnerung bleiben und dir ein Ansporn sein, die Jagd mit Demut, Leidenschaft und Verantwortung auszuüben.</p>
    <p>Mit diesem Jägerbrief gratulieren wir dir herzlich zu deinem ersten Feldhasen und wünschen dir weiterhin Waidmannsheil auf all deinen Wegen im Revier.</p>
  </div>

  <div class="hare-emblem" role="img" aria-label="Emblem: springender Feldhase vor Strahlenkranz über einem Schriftband"></div>

  <p class="closing greeting">Hochachtungsvoll und mit Waidmannsgruß</p>
  <p class="closing signature">Die Jagdgesellschaft von Birkenwöhrden</p>

  <div class="wax-seal" role="img" aria-label="Rotes Wachssiegel an einer Kordel"></div>
</main>
</body>
</html>
```